Small boutique multi-family apartment developer needs premium website design.

We are a growing real estate development company specializing in multi family apartment development. Our company Mireval Stone Development focuses on passive real estate investors looking to maximize their current real estate portfolio by allowing us to develop and reposition their current properties allowing them more cashflow while we are also able to take over the management of their asset in order to ensure optimal performance on a consistent basis.

```html
<!DOCTYPE html>
<html lang="en">
<head>
<meta charset="utf-8">
<title>Mireval Stone Development</title>
<link href="https://fonts.googleapis.com/css2?family=Poppins:wght@300;400;500;600;700&display=swap" rel="stylesheet">
<style>
:root{
  --ink:#23262f;
  --navy:#262a36;
  --accent:#c9a9b0;
  --accent-soft:#e8d8db;
  --muted:#6b6e78;
  --line:#d9d9de;
  --blush:#f6f2f2;
  --white:#ffffff;
}
*{margin:0;padding:0;box-sizing:border-box}
html,body{width:1200px;height:2607px;overflow:hidden}
body{position:relative;font-family:'Poppins',sans-serif;color:var(--ink);background:var(--white)}
.abs{position:absolute}
/* hero */
.hero{left:0;top:0;width:1200px;height:648px;background:linear-gradient(180deg,#2f3430 0%,#3d4636 35%,#4a4f3d 60%,#5b6246 80%,#4a4c45 100%)}
.hero-shade{left:0;top:0;width:1200px;height:648px;background:linear-gradient(90deg,rgba(20,22,26,.55),rgba(20,22,26,.15) 60%,rgba(20,22,26,.3))}
.socials{display:flex;gap:6px}
.social{position:relative;width:30px;height:30px;border:1px solid rgba(255,255,255,.85);display:flex;align-items:center;justify-content:center}
.social::before{content:"";position:absolute;left:-7px;top:14px;width:7px;height:1px;background:rgba(255,255,255,.85)}
.social i{width:6px;height:6px;border-radius:50%;background:var(--white)}
.social.on{background:var(--white)}
.social.on i{background:var(--accent)}
.foot .social{border-color:rgba(255,255,255,.7)}
.foot .social.on{background:var(--accent-soft)}
.foot .social.on i{background:var(--navy)}
.brand{color:var(--white);font-weight:500;font-size:15px;letter-spacing:.5px;display:flex;align-items:center;gap:8px}
.brand b{width:10px;height:10px;border:1.5px solid var(--white);display:block}
.nav{display:flex;gap:30px;font-size:10.5px;color:var(--white);letter-spacing:.3px}
.nav .cur{text-decoration:underline;text-underline-offset:4px}
.hero-frame{left:193px;top:245px;width:507px;height:403px;border-left:1px solid rgba(255,255,255,.7);border-top:1px solid rgba(255,255,255,.7)}
.hero-title{left:212px;top:306px;width:500px;color:var(--white);font-size:26px;font-weight:500;line-height:32.5px}
.btn{position:absolute;border:1px solid currentColor;font-size:10px;letter-spacing:.3px;display:flex;align-items:center;padding-left:18px}
.btn::before{content:"";position:absolute;left:0;top:50%;width:9px;height:1px;background:currentColor}
/* sections */
.label{font-size:11px;color:var(--accent)}
.rule{height:1px;background:var(--line)}
.h2{font-size:23px;font-weight:400;line-height:28px;color:var(--ink)}
.card{overflow:hidden}
.card-info{position:absolute;left:25px;bottom:22px;color:var(--white)}
.price{font-size:20px;font-weight:600}
.specs{font-size:9.5px;letter-spacing:.6px;margin-top:10px}
.desc{font-size:9.5px;margin-top:4px}
.fav{position:absolute;right:13px;top:14px;width:24px;height:24px;border-radius:50%;background:rgba(255,255,255,.85)}
.arrows{position:absolute;left:10px;top:8px;color:var(--white);font-size:12px}
.stats{left:0;top:1080px;width:1200px;height:262px;background:linear-gradient(180deg,#4f5360 0%,#6b6a72 40%,#4a4a52 75%,#3b3a3f 100%)}
.stat{position:absolute;top:1168px;width:208px;text-align:center;color:var(--white)}
.stat .n{font-size:48px;font-weight:700;color:#e4d7d9;line-height:60px}
.stat .t{font-size:13px;margin-top:-4px}
.stat-div{position:absolute;top:1178px;width:1px;height:66px;background:rgba(255,255,255,.4)}
.about-text{left:212px;top:1500px;width:374px;font-size:12.5px;line-height:21.2px;color:var(--muted);font-weight:300}
.about-text strong{color:var(--ink);font-weight:400}
.industry{left:0;top:1824px;width:1200px;height:486px;background:var(--blush)}
.svc{overflow:hidden}
.svc .num{position:absolute;left:18px;top:30px;color:var(--white);font-size:18px;font-weight:600}
.svc .name{position:absolute;left:18px;bottom:24px;color:var(--white);font-size:19px;font-weight:500;line-height:23px}
.foot{left:0;top:2310px;width:1200px;height:297px;background:var(--navy);color:var(--white)}
.fh{font-size:15.5px;font-weight:400;padding-bottom:3px;border-bottom:1px solid var(--white);display:inline-block}
.fi{font-size:10.5px;line-height:15px}
.field{position:absolute;border:1px solid rgba(255,255,255,.3);font-size:10.5px;color:rgba(255,255,255,.85);padding:9px 10px}
.chat{left:1120px;top:2545px;width:31px;height:31px;background:var(--accent-soft);display:flex;align-items:center;justify-content:center}
</style>
</head>
<body>

<!-- hero -->
<div class="abs hero" role="img" aria-label="Photo of a modern two-storey house with dark frames surrounded by trees and a lawn, a stepped stone path leading to the entrance"></div>
<div class="abs hero-shade"></div>
<div class="abs socials" style="left:194px;top:18px">
  <span class="social"><i></i></span><span class="social on"><i></i></span><span class="social"><i></i></span><span class="social"><i></i></span>
</div>
<div class="abs brand" style="left:510px;top:24px;width:180px;justify-content:center"><b></b>Mireval Stone</div>
<nav class="abs nav" style="left:777px;top:27px"><span class="cur">HOME</span><span>ABOUT</span><span>NEWS</span><span>CONTACT</span></nav>
<div class="abs hero-frame"></div>
<div class="abs brand" style="left:212px;top:272px;font-size:13px"><b></b>Mireval Stone</div>
<h1 class="abs hero-title">A Growing real estate development company specializing in multi-family apartment development.</h1>
<a class="btn" style="left:212px;top:428px;width:101px;height:31px;color:var(--white)">CONTACT US</a>
<svg class="abs" style="left:993px;top:604px" width="16" height="20" viewBox="0 0 16 20"><path d="M8 1V18M3 13L8 18L13 13" stroke="#fff" stroke-width="1.4" fill="none"/></svg>

<!-- properties -->
<div class="abs rule" style="left:0;top:715px;width:268px"></div>
<div class="abs label" style="left:278px;top:707px">Properties</div>
<h2 class="abs h2" style="left:193px;top:733px">Current Offered Properties</h2>
<div class="abs rule" style="left:1007px;top:992px;width:193px"></div>
<div class="abs card" style="left:193px;top:780px;width:397px;height:237px;background:linear-gradient(180deg,#1d3a8a 0%,#2a4a9a 35%,#5a5a68 65%,#3a3436 100%)" role="img" aria-label="Photo of a modern white house at dusk with a terrace, lounge seating and a fire pit">
  <span class="arrows">‹ ›</span><span class="fav"></span>
  <div class="card-info"><div class="price">$2,499,000</div><div class="specs"><b>3</b> BED &nbsp;|&nbsp; <b>2.5</b> BATH &nbsp;|&nbsp; <b>2,136</b> SQFT</div><div class="desc">Unobstructed Ocean and Bay view from every room.</div></div>
</div>
<div class="abs card" style="left:610px;top:780px;width:397px;height:237px;background:linear-gradient(180deg,#2e3440 0%,#4a4c52 40%,#6a5446 70%,#2e2a2a 100%)" role="img" aria-label="Photo of a modern multi-level house with warm lit windows among tall trees at dusk">
  <span class="arrows">‹ ›</span><span class="fav"></span>
  <div class="card-info"><div class="price">$2,500,000</div><div class="specs"><b>3</b> BED &nbsp;|&nbsp; <b>2.5</b> BATH &nbsp;|&nbsp; <b>2,136</b> SQFT</div><div class="desc">Unobstructed Ocean and Bay view from every room.</div></div>
</div>

<!-- stats -->
<div class="abs stats" role="img" aria-label="Photo of a layered modern house with glass balconies at sunset among pine trees"></div>
<div class="stat" style="left:184px"><div class="n">02</div><div class="t">Partners</div></div>
<div class="stat-div" style="left:392px"></div>
<div class="stat" style="left:392px"><div class="n">06</div><div class="t">Employees</div></div>
<div class="stat-div" style="left:600px"></div>
<div class="stat" style="left:600px"><div class="n">33</div><div class="t">Investments</div></div>
<div class="stat-div" style="left:808px"></div>
<div class="stat" style="left:808px"><div class="n">100%</div><div class="t">Success</div></div>

<!-- about -->
<div class="abs rule" style="left:0;top:1410px;width:268px"></div>
<div class="abs label" style="left:278px;top:1402px">About Us</div>
<h2 class="abs h2" style="left:193px;top:1428px">Welcome to the<br>Mireval Stone Development</h2>
<div class="abs" style="left:193px;top:1503px;width:1px;height:321px;background:var(--line)"></div>
<div class="abs about-text">
  <p><strong>Mireval Stone Development</strong> was created to satisfy the overwhelming request to help our clients who want to invest in long term buy and hold Real Estate, and create a more profitable and balanced investment portfolio. We offer opportunities to invest in cash flowing Multi-Family apartment building investments in the Southern California area.</p>
  <p style="margin-top:21px">"Many of our clients are looking to diversify their retirement portfolio, but don't know the ins and outs of how to invest in Managed Real Estate investments."</p>
</div>
<a class="btn" style="left:212px;top:1732px;width:100px;height:31px;color:var(--accent);border-color:var(--line)">LEARN MORE</a>
<div class="abs rule" style="left:1006px;top:1747px;width:194px"></div>
<div class="abs" style="left:653px;top:1405px;width:353px;height:358px;background:linear-gradient(180deg,#1a2ea8 0%,#2c3f9a 30%,#5a5e6e 60%,#3a3638 100%)" role="img" aria-label="Photo of a modern white house terrace at dusk with chairs and a glowing fire pit"></div>

<!-- industry -->
<div class="abs industry"></div>
<div class="abs rule" style="left:0;top:1891px;width:268px"></div>
<div class="abs label" style="left:278px;top:1883px">Industry</div>
<h2 class="abs h2" style="left:193px;top:1910px">Committed to the fundamentals of investing,<br>to ensure longterm growth</h2>
<div class="abs rule" style="left:1006px;top:2223px;width:194px"></div>
<div class="abs svc" style="left:193px;top:1990px;width:258px;height:258px;background:linear-gradient(160deg,#3c4654,#56606c 55%,#4a5460)" role="img" aria-label="Photo of a man examining an architectural model of an apartment tower">
  <span class="num">01.</span><span class="name">Apartment Building<br>Optimization</span></div>
<div class="abs svc" style="left:470px;top:1987px;width:259px;height:261px;background:linear-gradient(160deg,#4e5a60,#6a7276 55%,#545c62);border-bottom:4px solid var(--accent-soft)" role="img" aria-label="Photo of two colleagues reviewing plans next to a building model in an office">
  <span class="num">02.</span><span class="name">Real Estate Portfolio<br>Management</span></div>
<div class="abs svc" style="left:748px;top:1990px;width:258px;height:258px;background:linear-gradient(160deg,#6a6c74,#8a8a92 50%,#5e6068)" role="img" aria-label="Photo of a handshake over financial documents on a desk">
  <span class="num">03.</span><span class="name">Private<br>Lending</span></div>

<!-- footer -->
<footer class="abs foot" role="contentinfo">
  <div class="abs" style="left:0;top:110px;width:1200px;height:187px;background:linear-gradient(180deg,rgba(255,255,255,0),rgba(255,255,255,.04))" role="img" aria-label="Faint city skyline silhouette"></div>
  <div class="abs" style="left:193px;top:45px"><span class="fh">Contact Info</span></div>
  <svg class="abs" style="left:193px;top:84px" width="10" height="13" viewBox="0 0 10 13"><path d="M5 12C5 12 1 7.5 1 5A4 4 0 0 1 9 5C9 7.5 5 12 5 12Z" fill="none" stroke="#fff" stroke-width="1"/><circle cx="5" cy="5" r="1.4" fill="#fff"/></svg>
  <div class="abs fi" style="left:214px;top:83px">1840 Larkspur Way,<br>Suite 310, Harbor City,<br>CA. 90000</div>
  <svg class="abs" style="left:193px;top:141px" width="11" height="11" viewBox="0 0 11 11"><path d="M2 1L4 1L5 3.5L3.8 4.5C4.5 6 5 6.5 6.5 7.2L7.5 6L10 7V9C10 9.6 9.6 10 9 10C4.5 10 1 6.5 1 2C1 1.4 1.4 1 2 1Z" fill="none" stroke="#fff" stroke-width="1"/></svg>
  <div class="abs fi" style="left:214px;top:139px;text-decoration:underline">(555) 304-2718</div>
  <svg class="abs" style="left:193px;top:171px" width="11" height="9" viewBox="0 0 11 9"><rect x=".5" y=".5" width="10" height="8" fill="none" stroke="#fff"/><path d="M.5 .5L5.5 5L10.5 .5" fill="none" stroke="#fff"/></svg>
  <div class="abs fi" style="left:214px;top:168px">hello@mirevalstonedev.com</div>
  <div class="abs socials" style="left:200px;top:198px">
    <span class="social"><i></i></span><span class="social on"><i></i></span><span class="social"><i></i></span><span class="social"><i></i></span>
  </div>

  <div class="abs" style="left:426px;top:45px"><span class="fh">Quick Links</span></div>
  <div class="abs fi" style="left:427px;top:85px;font-size:10px;line-height:30px">
    <div style="text-decoration:underline">HOME</div><div>ABOUT US</div><div>NEWS</div><div>CONTACT US</div>
  </div>

  <div class="abs" style="left:609px;top:45px"><span class="fh">Send Us a Message</span></div>
  <div class="field" style="left:609px;top:83px;width:189px;height:32px">Name</div>
  <div class="field" style="left:816px;top:83px;width:190px;height:32px">Email</div>
  <div class="field" style="left:609px;top:126px;width:397px;height:63px">Message...</div>
  <a class="btn" style="left:906px;top:202px;width:100px;height:31px;color:var(--white);padding-left:32px;border-color:rgba(255,255,255,.7)">SUBMIT</a>

  <div class="abs" style="left:0;top:286px;width:1200px;text-align:center;font-size:9px;color:rgba(255,255,255,.85)">Copyright @ 2024 <span style="text-decoration:underline;color:var(--accent)">Mireval Stone Development</span>. All Rights Reserved.</div>
</footer>
<div class="abs chat"><svg width="14" height="12" viewBox="0 0 14 12"><path d="M1 1H13V9H5L2 11V9H1Z" fill="none" stroke="#262a36" stroke-width="1.1"/><path d="M4 4H10M4 6H9" stroke="#262a36"/></svg></div>

</body>
</html>
```